need 4 creative A frame (SANDWICH BOARD) designs concepts for dental office

need 4 creative A frame (SANDWICH BOARD) designs concepts
1 - targeting kids
2. targeting old age
3. targeting teens
4 targeting general public

website - www.pinecrestdental.ca

LINK for Measurements for sandwich board https://www.vordex.ca/KQ_4837/Steel-Clip-Rim-Folding-Board

i am attaching certain key ingredients ( rough sketch in uploaded files ) to be added on each design though not mandatory if the design is very creative

```html
<!DOCTYPE html>
<html lang="en">
<head>
<meta charset="UTF-8">
<title>Pinecrest Dental – A-Frame Board Concepts</title>
<link href="https://fonts.googleapis.com/css2?family=Montserrat:wght@400;600;700;800&family=Roboto+Condensed:wght@700&display=swap" rel="stylesheet">
<style>
  :root {
    --brand-blue: #29b6e8;
    --brand-blue-deep: #1593c9;
    --ink: #4a4a4c;
    --panel-dark: #2b2b2d;
    --panel-mid: #4a4b4e;
    --white: #ffffff;
    --page: #eef0f2;
  }
  * { box-sizing: border-box; margin: 0; padding: 0; }
  html, body { width: 1200px; height: 899px; overflow: hidden; }
  body {
    background: var(--page);
    font-family: "Montserrat", sans-serif;
    position: relative;
  }
  .board {
    position: absolute;
    top: 150px;
    width: 420px;
    height: 580px;
    background: var(--white);
    overflow: hidden;
    box-shadow: 0 6px 24px rgba(0,0,0,.18);
  }
  .board--braces { left: 150px; }
  .board--confident { left: 630px; }

  .board__shape { position: absolute; inset: 0; width: 100%; height: 100%; }

  .board__photo { position: absolute; }
  .board--braces .board__photo {
    left: 0; top: 0; width: 290px; height: 330px;
    background:
      linear-gradient(180deg, rgba(255,255,255,0) 60%, #fff 100%),
      linear-gradient(90deg, #7a4f33 0%, #b7845f 30%, #e8c3a4 60%, #f6e6da 85%, #fff 100%);
  }
  .board--confident .board__photo {
    right: 0; top: 0; width: 300px; height: 330px;
    background:
      linear-gradient(180deg, rgba(255,255,255,0) 60%, #fff 100%),
      linear-gradient(270deg, #5a7fb8 0%, #9bb6dd 25%, #efd3c3 55%, #f5ecef 80%, #fff 100%);
  }

  .headline { position: absolute; text-transform: uppercase; line-height: 1.05; }
  .headline__lead { color: var(--ink); font-weight: 800; }
  .headline__accent { color: var(--brand-blue); font-weight: 800; }

  .board--braces .headline { left: 255px; top: 24px; width: 160px; text-align: center; }
  .board--braces .headline__lead { font-size: 13px; line-height: 1.2; }
  .board--braces .headline__accent { font-size: 25px; margin-top: 10px; }

  .board--confident .headline { left: 28px; top: 40px; width: 190px; }
  .board--confident .headline__lead { font-size: 19px; line-height: 1.2; }
  .board--confident .headline__accent { font-size: 40px; margin-top: 4px; }

  .brand {
    position: absolute; left: 0; right: 0; top: 300px;
    display: flex; align-items: center; justify-content: center; gap: 8px;
  }
  .brand__dot { width: 14px; height: 14px; border-radius: 50%; background: var(--brand-blue); }
  .brand__name { font-size: 24px; font-weight: 600; color: var(--ink); letter-spacing: .5px; }

  .badge {
    position: absolute; top: 338px; width: 92px; height: 92px; border-radius: 50%;
    background: var(--brand-blue);
    border: 5px solid var(--white);
    box-shadow: 0 0 0 3px #9aa0a6, 0 4px 8px rgba(0,0,0,.35);
    display: flex; align-items: center; justify-content: center; text-align: center;
    color: var(--white); font-weight: 800; font-size: 13px; line-height: 1.2; text-transform: uppercase;
  }
  .badge--hours { left: 42px; }
  .badge--billing { right: 42px; }

  .welcome {
    position: absolute; left: 0; right: 0; top: 418px;
    display: flex; align-items: flex-end; justify-content: center; gap: 6px;
    font-family: "Roboto Condensed", sans-serif; text-transform: uppercase;
  }
  .welcome__stack { display: flex; flex-direction: column; align-items: flex-end; }
  .welcome__were { color: var(--white); font-size: 24px; line-height: 1; }
  .welcome__arrows { width: 70px; height: 20px; margin-top: 6px; }
  .welcome__in { color: var(--brand-blue); font-size: 62px; line-height: .85; }

  .intake {
    position: absolute; left: 50%; top: 486px; transform: translateX(-50%);
    padding: 4px 22px; border-radius: 14px;
    background: var(--brand-blue); color: var(--white);
    font-size: 15px; font-weight: 600; white-space: nowrap;
  }
  .phone {
    position: absolute; left: 0; right: 0; top: 520px; text-align: center;
    color: var(--brand-blue); font-size: 31px; font-weight: 400;
  }
  .phone strong { font-weight: 800; }
</style>
</head>
<body>

<section class="board board--braces">
  <div class="board__photo" role="img" aria-label="Photo of a smiling teenage girl with braces pointing at her teeth"></div>
  <svg class="board__shape" viewBox="0 0 420 580" preserveAspectRatio="none" aria-hidden="true">
    <defs>
      <linearGradient id="panelA" x1="0" y1="0" x2="0" y2="1">
        <stop offset="0" stop-color="#4a4b4e"/>
        <stop offset="1" stop-color="#232325"/>
      </linearGradient>
    </defs>
    <path d="M0 345 Q210 430 420 345 L420 372 Q210 452 0 372 Z" fill="#29b6e8"/>
    <path d="M0 368 Q210 448 420 368 L420 580 L0 580 Z" fill="url(#panelA)"/>
  </svg>
  <div class="headline">
    <p class="headline__lead">Healthy smile is cornerstone of every age</p>
    <p class="headline__accent">We love to care your smile</p>
  </div>
  <div class="brand"><span class="brand__dot"></span><span class="brand__name">Pinecrest Dental</span></div>
  <div class="badge badge--hours">Open<br>7<br>Days</div>
  <div class="badge badge--billing">We<br>Direct<br>Bill</div>
  <div class="welcome">
    <div class="welcome__stack">
      <span class="welcome__were">We're</span>
      <svg class="welcome__arrows" viewBox="0 0 70 20" aria-hidden="true">
        <g fill="none" stroke-width="4" stroke-linecap="square">
          <polyline points="12,3 4,10 12,17" stroke="#ffffff"/>
          <polyline points="28,3 20,10 28,17" stroke="#29b6e8"/>
          <polyline points="44,3 36,10 44,17" stroke="#29b6e8"/>
          <polyline points="60,3 52,10 60,17" stroke="#29b6e8"/>
        </g>
      </svg>
    </div>
    <span class="welcome__in">In</span>
  </div>
  <div class="intake">Accepting New Patient</div>
  <p class="phone">587 <strong>555 0142</strong></p>
</section>

<section class="board board--confident">
  <div class="board__photo" role="img" aria-label="Photo of a smiling young woman in a dental chair during a check-up"></div>
  <svg class="board__shape" viewBox="0 0 420 580" preserveAspectRatio="none" aria-hidden="true">
    <defs>
      <linearGradient id="panelB" x1="0" y1="0" x2="0" y2="1">
        <stop offset="0" stop-color="#4a4b4e"/>
        <stop offset="1" stop-color="#232325"/>
      </linearGradient>
    </defs>
    <path d="M0 345 Q210 430 420 345 L420 372 Q210 452 0 372 Z" fill="#29b6e8"/>
    <path d="M0 368 Q210 448 420 368 L420 580 L0 580 Z" fill="url(#panelB)"/>
  </svg>
  <div class="headline">
    <p class="headline__lead">Bring out the happy and confident</p>
    <p class="headline__accent">Smile</p>
  </div>
  <div class="brand"><span class="brand__dot"></span><span class="brand__name">Pinecrest Dental</span></div>
  <div class="badge badge--hours">Open<br>7<br>Days</div>
  <div class="badge badge--billing">We<br>Direct<br>Bill</div>
  <div class="welcome">
    <div class="welcome__stack">
      <span class="welcome__were">We're</span>
      <svg class="welcome__arrows" viewBox="0 0 70 20" aria-hidden="true">
        <g fill="none" stroke-width="4" stroke-linecap="square">
          <polyline points="12,3 4,10 12,17" stroke="#ffffff"/>
          <polyline points="28,3 20,10 28,17" stroke="#29b6e8"/>
          <polyline points="44,3 36,10 44,17" stroke="#29b6e8"/>
          <polyline points="60,3 52,10 60,17" stroke="#29b6e8"/>
        </g>
      </svg>
    </div>
    <span class="welcome__in">In</span>
  </div>
  <div class="intake">Accepting New Patient</div>
  <p class="phone">587 <strong>555 0142</strong></p>
</section>

</body>
</html>
```